High profile consulting company needs a Business Card Design

I need a business card design for a coaching /consulting company. We specialize in changing behaviors. Our services include therapy, workshops, life coaching, etc.

Check out our website to get a feel for our personality. www.tidewellpartners.com

The new logo will be attached to the website soon, I have attached the new logo for your use on the business card.
Updates

I forgot to provide you with the company email under the "must have" section for the business card.  The website is:

 www.tidewellpartners.com

I understand there's some trouble with the logo I uploaded.  I will try that again.  Thank you for your efforts.

Dalia

Thank you for some of your questions.  I prefer a one sided business card, and tend to like the white backgrounds.

I also made 2 small changes to the content.  

add MFT after the name:  Dalia Forsythe, MFT

and the tag line needed more clarity once I saw it.  Please change it to:  Improving performance by strengthening relationships and changing behaviors.

Thank you,
Dalia

Industry/Entity Type

Business

Requirements
Must have
• logo
Phone number: 321-555-0148
email: Dalia@tidewellpartners.com
Dalia Forsythe, MFT
President
Nice to have
• Improving performance by strengthening relationships and changing behaviors.

```html
<!DOCTYPE html>
<html lang="en">
<head>
<meta charset="utf-8">
<title>Tidewell Partners — Business Card</title>
<link href="https://fonts.googleapis.com/css2?family=Arimo:ital,wght@0,400;0,700;1,400&family=Tinos:ital,wght@1,700&family=PT+Sans&family=Courgette&display=swap" rel="stylesheet">
<style>
  :root {
    --backdrop: #e4e4e2;
    --card: #ffffff;
    --brand-green: #0f6e4f;
    --ink: #1b1b1b;
    --band-grey: #b9babc;
    --shadow: rgba(0,0,0,0.25);
  }
  * { box-sizing: border-box; margin: 0; padding: 0; }
  html, body {
    width: 1200px; height: 1074px; overflow: hidden;
    background: var(--backdrop);
  }
  .business-card {
    position: absolute;
    left: 67px; top: 232px;
    width: 1066px; height: 610px;
    background: var(--card);
    box-shadow: 0 6px 18px var(--shadow);
    overflow: hidden;
  }
  .brand {
    position: absolute; left: 82px; top: 38px;
    display: flex; align-items: center; gap: 22px;
  }
  .brand-mark {
    width: 134px; height: 134px; border-radius: 50%;
    border: 9px solid var(--brand-green);
  }
  .brand-name {
    font-family: "Arimo", Arial, sans-serif;
    font-weight: 700;
    font-size: 52px; line-height: 1.02;
    letter-spacing: 1px;
    color: var(--brand-green);
    text-transform: uppercase;
  }
  .person {
    position: absolute; left: 694px; top: 172px;
    color: var(--ink);
  }
  .person-name {
    font-family: "Tinos", "Times New Roman", serif;
    font-style: italic; font-weight: 700;
    font-size: 29px; line-height: 1.2;
  }
  .person-title, .person-phone {
    font-family: "Arimo", Arial, sans-serif;
    font-style: italic;
    font-size: 26px; line-height: 1.3;
  }
  .person-phone { display: flex; align-items: center; gap: 20px; }
  .contact-list {
    position: absolute; left: 108px; top: 326px;
    list-style: none;
    font-family: "PT Sans", "Myriad Pro", sans-serif;
    font-size: 27px; color: var(--ink);
  }
  .contact-list li { display: flex; align-items: center; gap: 34px; height: 38px; }
  .icon { width: 21px; height: 21px; flex: none; }
  .band { position: absolute; left: 0; top: 0; width: 1066px; height: 610px; }
  .tagline {
    position: absolute; right: 34px; top: 500px;
    text-align: right;
    font-family: "Courgette", cursive;
    font-size: 30px; line-height: 1.45;
    color: #ffffff;
    text-shadow: 1px 1px 0 #3a3a3a, -1px -1px 0 #3a3a3a, 1px -1px 0 #3a3a3a, -1px 1px 0 #3a3a3a;
  }
</style>
</head>
<body>
  <article class="business-card">
    <svg class="band" viewBox="0 0 1066 610" preserveAspectRatio="none" role="img" aria-label="Decorative grey and green swoosh band along the bottom of the card">
      <defs>
        <linearGradient id="band-fill" x1="0" x2="1" y1="0" y2="0">
          <stop offset="0" stop-color="#c4c5c7"/>
          <stop offset="0.55" stop-color="#b4b5b7"/>
          <stop offset="0.78" stop-color="#4f8a74"/>
          <stop offset="1" stop-color="#c2c4c4"/>
        </linearGradient>
      </defs>
      <path d="M0,500 C260,512 500,490 720,450 C860,425 980,410 1066,405 L1066,610 L0,610 Z" fill="url(#band-fill)"/>
    </svg>

    <header class="brand">
      <div class="brand-mark"></div>
      <h1 class="brand-name">Tidewell<br>Partners</h1>
    </header>

    <section class="person">
      <p class="person-name">Dalia Forsythe, MFT</p>
      <p class="person-title">President</p>
      <p class="person-phone">
        <svg class="icon" viewBox="0 0 20 20" aria-label="Phone">
          <circle cx="10" cy="10" r="8.5" fill="none" stroke="#0f6e4f" stroke-width="2"/>
          <path d="M7 5.5h2.2l.6 2.6-1.3.9a5 5 0 0 0 2.5 2.5l.9-1.3 2.6.6v2.2c-4.4.3-7.8-3.1-7.5-7.5z" fill="#0f6e4f"/>
        </svg>
        321-555-0148
      </p>
    </section>

    <ul class="contact-list">
      <li>
        <svg class="icon" viewBox="0 0 20 20" aria-label="Email">
          <rect x="2" y="4.5" width="16" height="11" fill="none" stroke="#0f6e4f" stroke-width="2"/>
          <path d="M2 5l8 6 8-6" fill="none" stroke="#0f6e4f" stroke-width="2"/>
        </svg>
        Dalia@tidewellpartners.com
      </li>
      <li>
        <svg class="icon" viewBox="0 0 20 20" aria-label="Website">
          <circle cx="10" cy="10" r="8" fill="none" stroke="#0f6e4f" stroke-width="2"/>
          <path d="M2 10h16M10 2v16M4 5.5h12M4 14.5h12" fill="none" stroke="#0f6e4f" stroke-width="1.5"/>
        </svg>
        www.tidewellpartners.com
      </li>
    </ul>

    <p class="tagline">A company specializeing in<br>changing behaviors</p>
  </article>
</body>
</html>
```